Business Card Design Project

We are rebranding an existing automotive collision repair business. The business is called dentworks garage. I have attached logo but I'm not tied to that. I want to leave this wide open.

I want this card to say we are professional, competent, cutting edge. We are focused on customers and use a lot of the latest technology to make the customer experience different. We sign customers in on iPads. Paperwork I signed electronically and updates are sent via text, email, logging on a website or as they wish. I want this innovation and image to come through in our cards

Target Market(s)

60%. Women 40% men. Age 35-60

Industry/Entity Type

Automotive

Requirements
Must have
• The card must have name, title, phone,email, cell, web page

```html
<!DOCTYPE html>
<html lang="en">
<head>
<meta charset="utf-8">
<title>Dentworks Garage – Business Card</title>
<link rel="stylesheet" href="https://fonts.googleapis.com/css2?family=Roboto:wght@400;500;700;900&family=Roboto+Condensed:wght@700&display=swap">
<style>
  :root {
    --page: #e6e4e1;
    --card-dark: #1b1b1b;
    --card-mid: #2c2c2c;
    --lime: #8cc63f;
    --lime-light: #a6d95a;
    --white: #ffffff;
    --text-soft: #eaeaea;
  }
  html, body {
    margin: 0;
    width: 1200px;
    height: 900px;
    overflow: hidden;
    background: var(--page);
  }
  .canvas {
    position: relative;
    width: 1200px;
    height: 900px;
  }
  .card {
    position: absolute;
    left: 250px;
    width: 700px;
    height: 400px;
    overflow: hidden;
    background:
      repeating-linear-gradient(90deg, rgba(255,255,255,0.025) 0 1px, transparent 1px 3px),
      linear-gradient(135deg, var(--card-mid), var(--card-dark) 60%, #141414);
    box-shadow: 0 8px 24px rgba(0,0,0,0.25);
  }
  .card-back { top: 33px; }
  .card-front { top: 467px; }

  .brand {
    font-family: "Roboto Condensed", "Roboto", sans-serif;
    font-weight: 700;
    color: var(--lime);
    white-space: nowrap;
    display: flex;
    align-items: center;
  }
  .brand-dot {
    display: inline-block;
    border-radius: 50%;
    background: var(--lime);
  }
  .card-back .brand {
    position: absolute;
    left: 0; right: 0; top: 0; bottom: 0;
    justify-content: center;
    font-size: 54px;
    gap: 16px;
  }
  .card-back .brand-dot { width: 22px; height: 22px; }

  .card-front .brand {
    position: absolute;
    right: 40px;
    top: 36px;
    font-size: 28px;
    gap: 10px;
  }
  .card-front .brand-dot { width: 12px; height: 12px; }

  .swoosh {
    position: absolute;
    left: 0; top: 0;
    width: 700px;
    height: 400px;
  }
  .person {
    position: absolute;
    left: 70px;
    top: 100px;
    font-family: "Roboto", sans-serif;
    white-space: nowrap;
  }
  .person-name {
    font-size: 56px;
    font-weight: 900;
    color: var(--lime);
    letter-spacing: 0.5px;
  }
  .person-title {
    font-size: 17px;
    font-weight: 700;
    color: var(--white);
    margin-left: 4px;
  }
  .address {
    position: absolute;
    left: 40px;
    bottom: 34px;
    margin: 0;
    font-family: "Roboto", sans-serif;
    font-size: 23px;
    line-height: 27px;
    color: var(--text-soft);
    font-style: normal;
  }
  .address .label { display: inline-block; width: 86px; }
  .web {
    position: absolute;
    right: 28px;
    bottom: 34px;
    text-align: right;
    font-family: "Roboto", sans-serif;
    font-weight: 700;
    font-size: 22px;
    line-height: 29px;
    color: var(--lime-light);
  }
</style>
</head>
<body>
<main class="canvas">
  <section class="card card-back" aria-label="Card back">
    <div class="brand"><span class="brand-dot"></span>dentworks garage</div>
  </section>

  <section class="card card-front" aria-label="Card front">
    <div class="brand"><span class="brand-dot"></span>dentworks garage</div>

    <svg class="swoosh" viewBox="0 0 700 400" aria-hidden="true">
      <path d="M0 178 C 200 150, 420 175, 700 285 L 700 300 C 430 195, 210 168, 0 192 Z" fill="var(--lime)"/>
      <path d="M0 192 C 210 168, 430 195, 700 300 L 700 306 C 420 210, 200 186, 0 204 Z" fill="var(--white)"/>
      <path d="M0 204 C 200 186, 420 210, 700 306 L 700 311 C 420 220, 200 196, 0 212 Z" fill="var(--lime)"/>
    </svg>

    <div class="person">
      <span class="person-name">Sam Carter</span><span class="person-title">, SALES REPRESENTATIVE</span>
    </div>

    <address class="address">
      ADDRESS LINE1<br>
      ADDRESS LINE2<br>
      <span class="label">Phone:</span>123-456-7890<br>
      <span class="label">Mob:</span>123-456-7890
    </address>

    <div class="web">
      sam@dentworksgarage.com<br>
      www.dentworksgarage.com
    </div>
  </section>
</main>
</body>
</html>
```